Business Card Design- Mortgage Firm

Looking to design a business Card for our Outside sales people. This card is used to provide their contact information to prospective clients and realtors. Must have All Pertinent company and licensing information by law. We are looking for a very modern design that flows with our current logo color scheme. Red/White/Black

Industry/Entity Type

Mortgage Lender

Contact Information for Business Card

Must stick with current color scheme.

Colors
f04a50
ffffff
ecf7fb

Requirements
Must have
• Company Logo or similar
• Company Address (547 W Larkin Avenue, Suite 318, Corona CA 92877 NMLS: 2947163)
• Agent Name (Nora Pell)
• Title (Senior Mortgage Loan Originator)
• NMLS# 7395281
• Toll Free: 800-627-3184
• Direct : 310-555-8347
Nice to have
• Room for Agent Picture

```html
<!DOCTYPE html>
<html lang="en">
<head>
<meta charset="utf-8">
<title>Crestline Home Loans – Business Card</title>
<link rel="stylesheet" href="https://fonts.googleapis.com/css2?family=Open+Sans:wght@400;600;700&display=swap">
<style>
  :root {
    --stage: #1d1d1f;
    --brand-red: #b3242b;
    --brand-red-dark: #9c1e25;
    --card-white: #f4f4f4;
    --ink: #2a2a2a;
    --rule: #3a3a3a;
  }
  * { box-sizing: border-box; margin: 0; padding: 0; }
  html, body {
    width: 1200px; height: 904px; overflow: hidden;
    background: var(--stage);
    font-family: "Open Sans", Arial, sans-serif;
  }
  .stage {
    position: relative; width: 1200px; height: 904px;
    display: flex; flex-direction: column; align-items: center; justify-content: center; gap: 56px;
  }
  .card {
    position: relative; width: 640px; height: 366px;
    border-radius: 22px; overflow: hidden;
    box-shadow: 0 14px 30px rgba(0,0,0,.45);
  }
  /* Back side */
  .card--back {
    background: linear-gradient(160deg, #b8272e 0%, var(--brand-red-dark) 100%);
    display: flex; align-items: center; justify-content: center; gap: 14px;
  }
  .back-mark { width: 26px; height: 26px; background: #fff; }
  .back-wordmark { color: #fff; font-weight: 700; font-size: 30px; letter-spacing: 1px; }

  /* Front side */
  .card--front { background: linear-gradient(180deg, #fbfbfb 0%, #e9e9e9 100%); }
  .front-band {
    position: absolute; left: 0; right: 0; bottom: 0; height: 16px; background: var(--brand-red);
  }
  .brand {
    position: absolute; left: 40px; top: 64px;
    display: flex; align-items: center; gap: 10px;
  }
  .brand-mark { width: 18px; height: 18px; background: var(--brand-red); }
  .brand-name { color: var(--brand-red); font-weight: 700; font-size: 24px; letter-spacing: .5px; }
  .brand-rule {
    position: absolute; left: 330px; right: 40px; top: 50px; height: 1px; background: var(--rule);
  }
  .agent { position: absolute; left: 44px; top: 186px; }
  .agent-name { color: var(--brand-red); font-weight: 700; font-size: 20px; line-height: 1.1; }
  .agent-title { color: var(--ink); font-size: 14px; margin-top: 2px; }
  .agent-rule { position: absolute; left: 44px; top: 240px; width: 268px; height: 1px; background: var(--rule); }
  .contact { color: var(--ink); font-size: 14.5px; line-height: 1.45; }
  .contact--office { position: absolute; left: 44px; top: 252px; }
  .contact--direct { position: absolute; left: 344px; top: 186px; }
  .column-rule { position: absolute; left: 326px; top: 190px; width: 1px; height: 96px; background: var(--rule); }
</style>
</head>
<body>
  <main class="stage">
    <section class="card card--back" aria-label="Card back">
      <span class="back-mark"></span>
      <span class="back-wordmark">Crestline Home Loans</span>
    </section>

    <section class="card card--front" aria-label="Card front">
      <div class="brand-rule"></div>
      <div class="brand">
        <span class="brand-mark"></span>
        <span class="brand-name">Crestline Home Loans</span>
      </div>

      <div class="agent">
        <p class="agent-name">Nora Pell</p>
        <p class="agent-title">Senior Mortgage Loan Originator</p>
      </div>
      <div class="agent-rule"></div>

      <address class="contact contact--office" style="font-style:normal">
        547 W Larkin Avenue, Suite 318<br>
        Corona CA 92877<br>
        NMLS: 2947163
      </address>

      <div class="column-rule"></div>

      <div class="contact contact--direct">
        NMLS# 7395281<br>
        800-627-3184 (Toll Free)<br>
        310-555-8347 (Direct)
      </div>

      <div class="front-band"></div>
    </section>
  </main>
</body>
</html>
```